I need a business card for myself, being a proprietor of a funeral parlor based in Manila. I'd like the card to have either of the following:
White Font on Black Background
or
Black Font on White Background
No logo is needed however I will appreciate any efforts to show a symbol of eternal happiness, aptly designed with above mentioned colors in mind.
Company name, address and contact on the lower right corner.
Logo or symbol anywhere.
Quillstone Funeral Services
+639174826351
darvik4521@pelmora.com
corner of Brisco Avenue and Velhurst Street
Makati City, Philippines
Thank you.
Update: Please include a small dove in your design. You are free to choose where you would like it on the card.

```html
<!DOCTYPE html>
<html lang="en">
<head>
<meta charset="utf-8">
<title>Quillstone Funeral Services – Business Card</title>
<link href="https://fonts.googleapis.com/css2?family=Open+Sans:wght@400;700&display=swap" rel="stylesheet">
<style>
  :root {
    --backdrop: #1c1c1c;
    --card: #ffffff;
    --card-shade: #e6e6e6;
    --ink: #161616;
    --rule: #9a9a9a;
  }
  * { margin: 0; padding: 0; box-sizing: border-box; }
  html, body {
    width: 1200px;
    height: 1200px;
    overflow: hidden;
    background: var(--backdrop);
  }
  .business-card {
    position: absolute;
    left: 100px;
    top: 314px;
    width: 1000px;
    height: 572px;
    background: radial-gradient(ellipse at 30% 40%, var(--card) 55%, var(--card-shade) 100%);
    font-family: "Open Sans", Arial, sans-serif;
    color: var(--ink);
  }
  .emblem {
    position: absolute;
    left: 575px;
    top: 110px;
    width: 64px;
    height: 64px;
    border-radius: 50%;
    background: var(--ink);
  }
  .brand {
    position: absolute;
    left: 530px;
    top: 196px;
    font-weight: 700;
    line-height: 1;
  }
  .brand-main { display: block; font-size: 64px; letter-spacing: -1px; }
  .brand-sub { display: block; font-size: 38px; margin-top: 4px; letter-spacing: 1px; }
  .contact-list {
    position: absolute;
    left: 534px;
    top: 352px;
    list-style: none;
    font-size: 19px;
    font-weight: 400;
    line-height: 1.3;
  }
  .contact-item {
    display: flex;
    align-items: flex-start;
    gap: 12px;
    padding: 3px 0;
  }
  .contact-item.ruled { border-bottom: 1px solid var(--rule); width: 300px; }
  .contact-icon { width: 16px; height: 16px; flex: none; margin-top: 4px; }
</style>
</head>
<body>
  <section class="business-card">
    <div class="emblem" role="img" aria-label="Small dove carrying an olive branch"></div>
    <h1 class="brand">
      <span class="brand-main">Quillstone</span>
      <span class="brand-sub">Funeral Services</span>
    </h1>
    <ul class="contact-list">
      <li class="contact-item ruled">
        <svg class="contact-icon" viewBox="0 0 16 16" aria-hidden="true"><path d="M3 1h3l1.5 4-2 1.3a9 9 0 0 0 4.2 4.2L11 8.5l4 1.5v3a2 2 0 0 1-2 2A12 12 0 0 1 1 3a2 2 0 0 1 2-2z" fill="var(--ink)"/></svg>
        <span>+639174826351</span>
      </li>
      <li class="contact-item ruled">
        <svg class="contact-icon" viewBox="0 0 16 16" aria-hidden="true"><rect x="1" y="3" width="14" height="10" fill="none" stroke="var(--ink)" stroke-width="1.4"/><path d="M1 3l7 6 7-6" fill="none" stroke="var(--ink)" stroke-width="1.4"/></svg>
        <span>darvik4521@pelmora.com</span>
      </li>
      <li class="contact-item">
        <svg class="contact-icon" viewBox="0 0 16 16" aria-hidden="true"><path d="M8 0a5.5 5.5 0 0 0-5.5 5.5C2.5 10 8 16 8 16s5.5-6 5.5-10.5A5.5 5.5 0 0 0 8 0zm0 8a2.5 2.5 0 1 1 0-5 2.5 2.5 0 0 1 0 5z" fill="var(--ink)"/></svg>
        <span>corner of Brisco Avenue and Velhurst<br>Street Makati City, Philippines</span>
      </li>
    </ul>
  </section>
</body>
</html>
```